Cherry Avenue the Musical Poster

We need a poster design for a high school production of Cherry Avenue the Musical. Simple, Clean, Glamorous, Bold. Lots of empty space for the required text included in the document attached. We would like the color scheme to be pink, black, and sparkle.

We are envisioning a script font or a college block style font or a combination of the two with a look that pops on a black or hot pink background.

The overall dimensions of the project need to be 11x17, 300 dpi for printing. I have included a document that describes the crop/bleed specifications.

After we decide on artwork for the poster, we need to include the following details on the poster, some of which are contractually mandatory and others provide details about attending the show.
I have included the specifications from the licensing company which state the approximate proportional size of each of the required elements describing the show.

```html
<!DOCTYPE html>
<html lang="en">
<head>
<meta charset="utf-8">
<title>Cherry Avenue – Maple Crest High School Theatre Company</title>
<link href="https://fonts.googleapis.com/css2?family=Abril+Fatface&family=Cinzel:wght@400;600&display=swap" rel="stylesheet">
<style>
  :root {
    --bg-top: #6f1f45;
    --bg-mid: #4d1f45;
    --bg-bottom: #231838;
    --panel-top: #cc1d62;
    --panel-bottom: #a61d5e;
    --band: #8e1c45;
    --spark-gold: #f0b020;
    --spark-orange: #e77a22;
    --ink: #ffffff;
  }
  * { margin: 0; padding: 0; box-sizing: border-box; }
  html, body { width: 776px; height: 1200px; overflow: hidden; background: var(--bg-bottom); }
  .poster {
    position: relative; width: 776px; height: 1200px; overflow: hidden;
    background: linear-gradient(180deg, var(--bg-top) 0%, var(--bg-mid) 55%, var(--bg-bottom) 100%);
    color: var(--ink);
    font-family: "Cinzel", "Times New Roman", serif;
  }
  .sparkle-field {
    position: absolute; left: -60px; top: -40px; width: 520px; height: 680px;
    background: radial-gradient(ellipse at 55% 45%, rgba(240,176,32,0.0) 12%, rgba(240,176,32,0.55) 30%, rgba(231,122,34,0.45) 48%, rgba(231,122,34,0) 70%);
  }
  .panel {
    position: absolute; left: 168px; top: 103px; right: 0; height: 990px;
    background: linear-gradient(180deg, var(--panel-top) 0%, var(--panel-bottom) 100%);
    opacity: 0.92;
  }
  .panel-band {
    position: absolute; left: 168px; right: 0; top: 494px; height: 16px;
    background: var(--band); opacity: 0.85;
  }
  .presenter {
    position: absolute; left: 168px; right: 0; top: 132px;
    text-align: center; font-size: 20.5px; font-weight: 600; line-height: 29px; letter-spacing: 0.3px;
  }
  .title {
    position: absolute; left: 168px; right: 0; top: 196px;
    font-family: "Abril Fatface", "Didot", serif; font-weight: 400;
    text-align: center; font-size: 118px; line-height: 112px;
    text-shadow: 3px 5px 6px rgba(90,10,40,0.55);
  }
  .mic-art {
    position: absolute; left: 55px; top: 495px; width: 215px; height: 598px;
    background: linear-gradient(180deg, rgba(255,255,255,0.28), rgba(255,255,255,0.12));
    border-radius: 100px 100px 6px 6px;
  }
  .credit { position: absolute; left: 384px; }
  .icon { position: absolute; fill: none; stroke: var(--ink); stroke-width: 2.2; }
  .label { font-size: 23px; line-height: 30px; letter-spacing: 0.5px; }
  .name { font-size: 29px; line-height: 34px; font-weight: 600; letter-spacing: 0.6px; }
  .amp { font-size: 19px; line-height: 20px; }
  .source { font-size: 18px; line-height: 25px; margin-top: 6px; letter-spacing: 0.4px; }
  .dates { font-size: 29px; line-height: 38px; font-weight: 600; }
  .tickets { font-size: 30px; line-height: 36px; font-weight: 600; }
  .url { font-size: 19px; line-height: 26px; font-weight: 600; margin-top: 8px; }
  .licence {
    position: absolute; left: 140px; right: 34px; top: 1114px;
    font-size: 10.6px; line-height: 15px; text-align: justify; text-align-last: justify; letter-spacing: 0.2px;
  }
</style>
</head>
<body>
<div class="poster">
  <div class="sparkle-field" role="img" aria-label="Radiating field of gold and orange sparkle dots"></div>
  <div class="panel"></div>
  <div class="panel-band"></div>

  <p class="presenter">Maple Crest High School Theatre Company<br>Presents</p>
  <h1 class="title">Cherry<br>Avenue</h1>

  <div class="mic-art" role="img" aria-label="White line illustration of a vintage stage microphone"></div>

  <svg class="icon" style="left:298px;top:527px" width="66" height="66" viewBox="0 0 66 66">
    <circle cx="33" cy="33" r="14"/>
    <path d="M28 39v-11l10-3v11"/><circle cx="26" cy="39" r="2.2"/><circle cx="36" cy="36" r="2.2"/>
    <path d="M6 28v10M11 24v18M16 20v26M50 20v26M55 24v18M60 28v10M27 6v7M33 3v10M39 6v7M27 53v7M33 53v10M39 53v7"/>
  </svg>
  <div class="credit" style="top:540px">
    <p class="label">Music and Lyrics by</p>
    <p class="name" style="margin-top:10px">Daniel Whitlow</p>
    <p class="amp">&amp;</p>
    <p class="name" style="margin-top:2px">Rosa Kendrick</p>
  </div>

  <svg class="icon" style="left:294px;top:690px" width="72" height="64" viewBox="0 0 72 64">
    <path d="M4 20l28 14 24-26M4 20l-2 6 30 16 28-28-4-4M32 34l0 8"/>
    <path d="M50 10v-8l10-2v8"/><circle cx="48" cy="11" r="2"/><circle cx="58" cy="9" r="2"/>
  </svg>
  <div class="credit" style="top:698px">
    <p class="label">Book by</p>
    <p class="name" style="margin-top:8px">Miriam Ostrow</p>
    <p class="source">Based on the novel by<br>Clara Wendell and<br>The Silverline Pictures<br>Motion Picture</p>
  </div>

  <svg class="icon" style="left:292px;top:900px" width="74" height="70" viewBox="0 0 74 70">
    <rect x="3" y="8" width="66" height="58" rx="7"/><path d="M3 22h66M18 3v10M54 3v10"/>
    <g fill="#fff" stroke="none"><rect x="14" y="30" width="10" height="9"/><rect x="31" y="30" width="10" height="9"/><rect x="48" y="30" width="10" height="9"/><rect x="14" y="45" width="10" height="9"/><rect x="31" y="45" width="10" height="9"/><rect x="48" y="45" width="10" height="9"/></g>
  </svg>
  <div class="credit" style="top:903px;left:382px">
    <p class="dates">April 22, 23, 29, 30</p>
    <p class="dates">7:00 PM</p>
  </div>

  <svg class="icon" style="left:293px;top:1010px" width="72" height="72" viewBox="0 0 72 72">
    <path d="M4 48L48 4l8 8a6 6 0 0 0 8 8l4 4L24 68l-4-4a6 6 0 0 0-8-8z"/><path d="M38 14l22 22" stroke-dasharray="2 4"/>
  </svg>
  <div class="credit" style="top:1008px;left:381px">
    <p class="tickets">Tickets</p>
    <p class="url">mchs.seatpass.com</p>
  </div>

  <p class="licence">Cherry Avenue is presented through special arrangement with Stagecraft Licensing Group (SLG). All authorized performance materials are also supplied by SLG. www.slgshows.com</p>
</div>
</body>
</html>
```